Letterhead designs for Property Management firm

Would like to see some different letterhead/envelope designs We are a residential property management company. We would like to see designs that utilize blue/grays/black

```html
<!DOCTYPE html>
<html lang="en">
<head>
<meta charset="utf-8">
<title>Harborline Property Management – Stationery</title>
<link href="https://fonts.googleapis.com/css2?family=Questrial&family=Roboto:wght@400&display=swap" rel="stylesheet">
<style>
  :root {
    --backdrop: #dcdcdc;
    --paper: #f6f6f6;
    --brand-blue: #0055a6;
    --ink: #3a3a3a;
    --ink-soft: #555555;
    --rule: #bdbdbd;
    --white: #ffffff;
  }
  * { margin: 0; padding: 0; box-sizing: border-box; }
  html, body { width: 1200px; height: 877px; overflow: hidden; }
  body {
    background: var(--backdrop);
    position: relative;
    font-family: "Questrial", sans-serif;
    color: var(--ink);
  }

  .sheet {
    position: absolute;
    background: linear-gradient(90deg, #f8f8f8, #f3f3f3);
    box-shadow: 0 2px 10px rgba(0,0,0,0.18);
  }

  /* Letterhead */
  .letterhead { left: 69px; top: 64px; width: 527px; height: 742px; }
  .brand-name {
    position: absolute;
    font-family: "Questrial", sans-serif;
    color: var(--brand-blue);
    text-align: center;
    line-height: 1.05;
  }
  .letterhead .brand-name { left: 46px; top: 52px; width: 110px; font-size: 18px; }
  .brand-name small { display: block; font-size: 9.5px; letter-spacing: 0.3px; margin-top: 3px; }

  .contact-rule {
    position: absolute; left: 377px; top: 50px; width: 1px; height: 60px;
    background: var(--rule);
  }
  .contact {
    position: absolute; left: 391px; top: 49px;
    font-family: "Roboto", sans-serif; font-size: 7.6px; color: var(--ink-soft);
    line-height: 9.8px; list-style: none;
  }
  .contact li { display: flex; align-items: center; gap: 4px; }
  .contact .address { margin-bottom: 2.5px; }
  .contact svg { width: 7px; height: 7px; fill: var(--brand-blue); flex: none; }

  .salutation { position: absolute; left: 46px; top: 205px; font-size: 13.5px; color: var(--ink); }
  .letter-body {
    position: absolute; left: 46px; top: 247px; width: 438px;
    font-size: 7.7px; line-height: 11.35px; color: var(--ink-soft);
    text-align: justify;
  }
  .letter-body p { margin-bottom: 11.35px; }
  .closing { position: absolute; left: 46px; top: 486px; font-size: 7.7px; color: var(--ink-soft); }
  .signature {
    position: absolute; left: 41px; top: 518px; width: 96px; height: 38px;
    background: linear-gradient(90deg, rgba(0,85,166,0.15), rgba(0,85,166,0.05));
    border-radius: 4px;
  }
  .footer-line { position: absolute; left: 0; width: 100%; height: 1px; background: var(--brand-blue); }
  .footer-band {
    position: absolute; left: 0; width: 100%; background: var(--brand-blue);
    color: var(--white); text-align: center;
  }
  .letterhead .footer-line { top: 723px; }
  .letterhead .footer-band {
    top: 726px; height: 16px; font-family: "Roboto", sans-serif;
    font-size: 7.5px; letter-spacing: 3px; line-height: 16px;
  }

  /* Envelope back */
  .envelope-back { left: 614px; top: 269px; width: 531px; height: 241px; background: var(--paper); }
  .flap { position: absolute; left: 0; top: 0; width: 531px; height: 74px; }
  .flap path { fill: var(--brand-blue); }
  .flap-name {
    position: absolute; left: 0; top: 32px; width: 100%; text-align: center;
    font-size: 12px; color: var(--white);
  }

  /* Envelope front */
  .envelope-front { left: 614px; top: 562px; width: 532px; height: 243px; }
  .envelope-front .brand-name { left: 30px; top: 26px; width: 106px; font-size: 18px; }
  .return-address {
    position: absolute; left: 33px; top: 98px; width: 100px; text-align: center;
    font-family: "Roboto", sans-serif; font-size: 7.6px; line-height: 9.6px; color: var(--ink-soft);
  }
  .envelope-front .footer-line { top: 223px; }
  .envelope-front .footer-band { top: 226px; height: 17px; }
</style>
</head>
<body>

  <section class="sheet letterhead">
    <div class="brand-name">Harborline<small>Property Management</small></div>

    <div class="contact-rule"></div>
    <ul class="contact">
      <li class="address">2140 Birchwood Court<br>Juneau, Alaska 99801</li>
      <li><svg viewBox="0 0 10 10"><path d="M2 0.5 L4 2.5 L3 4 Q4.5 6 6 7 L7.5 6 L9.5 8 L8 9.5 Q4 9 0.5 2 Z"/></svg>907 555 0142</li>
      <li><svg viewBox="0 0 10 10"><path d="M2.5 0 H7.5 V10 H2.5 Z M3.5 1 V8 H6.5 V1 Z"/></svg>907 555 0187</li>
      <li><svg viewBox="0 0 10 10"><path d="M3 0.5 H7 V3 H3 Z M0.5 3.5 H9.5 V7.5 H0.5 Z M2.5 8 H7.5 V9.5 H2.5 Z"/></svg>907 555 0163</li>
      <li><svg viewBox="0 0 10 10"><path d="M0.5 2 H9.5 V8 H0.5 Z M1 2.5 L5 5.5 L9 2.5" stroke="#fff" stroke-width="0.6"/></svg>hello@harborlinepm.com</li>
    </ul>

    <p class="salutation">Dear Mr. Hart,</p>
    <div class="letter-body">
      <p>Lorem ipsum dolor sit amet, consectetur adipiscing elit. Donec orci purus, luctus vitae dignissim eu, iaculis sed purus. Vivamus faucibus, ipsum nec aliquet viverra, leo mauris condimentum ligula, sit amet sagittis enim ligula quis arcu. Nam egestas tortor id nisi porttitor mattis. In tortor ante, ultricies in suscipit a, tempus non massa. Vivamus et auctor mi. Fusce vel massa nulla. Phasellus nec eros mauris, et scelerisque orci.</p>
      <p>Donec malesuada orci vitae nulla accumsan porta a id massa. Quisque accumsan iaculis magna sit amet fringilla. Maecenas consequat, magna eget tincidunt semper, odio nibh rutrum mi, id feugiat ante nisi eu risus. Vestibulum nunc orci, rhoncus a placerat in, ultricies in mi. Cras mattis varius eros, vel fringilla nisi suscipit eget. Quisque scelerisque sagittis nulla at porttitor.</p>
      <p>Sed id augue vitae urna euismod commodo aliquet a quam. Pellentesque arcu velit, cursus et malesuada ut, consequat et diam. Nullam erat sem, rhoncus id ullamcorper vitae, rhoncus et arcu. In ultricies ultricies nulla, ut rutrum nisi iaculis at. Donec eu magna a metus ornare faucibus. Fusce aliquet faucibus ultricies. Morbi semper, est id tincidunt gravida, sem arcu adipiscing lacus, ac bibendum nulla leo eu purus. Quisque nec diam sed risus consectetur a ccumsan quis quis nibh. Vestibulum id purus lorem.</p>
      <p>It is a long established fact that a reader will be distracted by the readable content of a page when looking at its layout. The point of using Lorem Ipsum is that it has a more-or-less normal distribution of letters, as opposed to using 'Content here, content here', making it look like readable English. Many desktop publishing packages</p>
    </div>
    <p class="closing">Sincerely,</p>
    <div class="signature" role="img" aria-label="Handwritten signature of Daniel Hart"></div>

    <div class="footer-line"></div>
    <div class="footer-band">www.harborlinepm.com</div>
  </section>

  <section class="sheet envelope-back">
    <svg class="flap" viewBox="0 0 531 74" aria-hidden="true">
      <path d="M0 0 H531 L524 34 Q516 74 474 74 H57 Q15 74 7 34 Z"/>
    </svg>
    <div class="flap-name">Harborline</div>
  </section>

  <section class="sheet envelope-front">
    <div class="brand-name">Harborline<small>Property Management</small></div>
    <p class="return-address">2140 Birchwood Court<br>Juneau, Alaska 99801</p>
    <div class="footer-line"></div>
    <div class="footer-band"></div>
  </section>

</body>
</html>
```